Velbrook Naturals - High Quality Organic Cleaning Product

A product label for a foaming hand soap. Company is called "Velbrook Naturals" and the tagline is "Naturally Pure Clean". Maybe lighter blue background with red letters, but open to what looks good. Want it to be a simple, clean and sophisticated design that looks fresh and stands out. This product has high quality organic ingredients hence the ingredients are "velbrook naturals" than other toxic chemical cleaners. Attached is label specifications as well as an image for stock language for left and right side of label for reference. Parts can be omitted, added or mixed and matched as needed.
Went on vacation/holiday
Moms

```html
<!DOCTYPE html>
<html lang="en">
<head>
<meta charset="UTF-8">
<title>Velbrook Naturals – Foaming Hand Soap Label</title>
<link href="https://fonts.googleapis.com/css2?family=Montserrat:ital,wght@0,500;0,600;1,600&family=DM+Serif+Display&display=swap" rel="stylesheet">
<style>
  :root {
    --backdrop: #fdb4b3;
    --label: #ffffff;
    --brand-blue: #1b67b2;
    --panel-blue: #1a63ad;
    --accent-red: #d9213a;
    --ink: #2a2a2a;
    --panel-text: #dce8f5;
  }
  * { margin: 0; padding: 0; box-sizing: border-box; }
  html, body { width: 1200px; height: 1200px; overflow: hidden; }
  body {
    background: var(--backdrop);
    display: flex;
    align-items: center;
    justify-content: center;
    font-family: "Montserrat", sans-serif;
  }
  .label {
    position: relative;
    width: 720px;
    height: 960px;
    background: var(--label);
    border-radius: 18px;
    overflow: hidden;
  }
  .top-rule {
    position: absolute;
    top: 120px;
    left: 0;
    right: 0;
    height: 12px;
    background: var(--accent-red);
  }
  .brand {
    position: absolute;
    top: 150px;
    left: 0;
    right: 0;
    text-align: center;
  }
  .brand-name {
    color: var(--brand-blue);
    font-weight: 600;
    font-size: 40px;
    letter-spacing: 4px;
    line-height: 1.15;
    text-transform: uppercase;
  }
  .tagline {
    margin-top: 16px;
    color: var(--ink);
    font-weight: 600;
    font-style: italic;
    font-size: 18px;
    letter-spacing: 1px;
  }
  .product-title {
    position: absolute;
    top: 390px;
    left: 0;
    right: 0;
    text-align: center;
    font-family: "DM Serif Display", serif;
    font-weight: 400;
  }
  .product-main {
    display: block;
    color: var(--brand-blue);
    font-size: 116px;
    line-height: 1;
  }
  .product-sub {
    display: block;
    color: var(--accent-red);
    font-size: 56px;
    line-height: 1;
    margin-top: -8px;
    margin-left: -130px;
  }
  .claims-panel {
    position: absolute;
    left: 40px;
    right: 40px;
    bottom: 40px;
    height: 250px;
    background: var(--panel-blue);
    border-radius: 22px;
    padding: 40px 30px 0;
  }
  .claims {
    display: flex;
    justify-content: space-between;
    list-style: none;
  }
  .claim {
    flex: 1;
    text-align: center;
    color: var(--panel-text);
    font-size: 13px;
    position: relative;
  }
  .claim + .claim::before {
    content: "";
    position: absolute;
    left: 0;
    top: 18px;
    height: 60px;
    width: 2px;
    background: var(--panel-text);
    opacity: .6;
  }
  .claim svg { width: 64px; height: 64px; display: block; margin: 0 auto 12px; }
  .net-weight {
    text-align: center;
    color: var(--panel-text);
    font-size: 30px;
    margin-top: 34px;
  }
</style>
</head>
<body>
  <main class="label">
    <div class="top-rule"></div>

    <header class="brand">
      <div class="brand-name">Velbrook<br>Naturals</div>
      <p class="tagline">Naturally Pure Clean</p>
    </header>

    <h1 class="product-title">
      <span class="product-main">Foaming</span>
      <span class="product-sub">Hand Soap</span>
    </h1>

    <section class="claims-panel">
      <ul class="claims">
        <li class="claim">
          <svg viewBox="0 0 64 64" fill="none" stroke="#dce8f5" stroke-width="3">
            <circle cx="32" cy="32" r="28"/>
            <path d="M32 46 C22 44 18 34 20 24 C28 26 32 34 32 46Z"/>
            <path d="M32 46 C42 44 46 34 44 24 C36 26 32 34 32 46Z"/>
          </svg>
          ALL-Natural
        </li>
        <li class="claim">
          <svg viewBox="0 0 64 64" fill="none" stroke="#dce8f5" stroke-width="3">
            <circle cx="32" cy="32" r="28"/>
            <path d="M27 16 H37 M29 16 V28 L20 44 Q19 48 23 48 H41 Q45 48 44 44 L35 28 V16"/>
          </svg>
          Paraben Free
        </li>
        <li class="claim">
          <svg viewBox="0 0 64 64" fill="none" stroke="#dce8f5" stroke-width="3">
            <circle cx="32" cy="32" r="28"/>
            <path d="M32 48 C20 42 20 24 32 14 C44 24 44 42 32 48Z"/>
            <path d="M32 22 V48"/>
          </svg>
          100% Vegan
        </li>
        <li class="claim">
          <svg viewBox="0 0 64 64" fill="none" stroke="#dce8f5" stroke-width="3">
            <circle cx="32" cy="32" r="28"/>
            <circle cx="32" cy="32" r="14"/>
            <path d="M22 22 L42 42"/>
          </svg>
          Cruelty Free
        </li>
      </ul>
      <p class="net-weight">12 oz</p>
    </section>
  </main>
</body>
</html>
```